Magazine site

We are replacing this site www.thebrackmoorbuilder.com to almost be exactly like timberlandsweekly.com and theplankettfitter.com, except the engineer will display a blog article on the home page.
Updates

Industry/Entity Type

Engineer

Requirements
Must have
• Blog Article

```html
<!DOCTYPE html>
<html lang="en">
<head>
<meta charset="utf-8">
<title>The Brackmoor Builder</title>
<link href="https://fonts.googleapis.com/css2?family=Ubuntu:wght@400;500;700&family=Arimo:ital,wght@0,400;0,700;1,400;1,700&display=swap" rel="stylesheet">
<style>
:root{
  --red:#b3111b;
  --red-bright:#e0202a;
  --red-dark:#8a0c12;
  --ink:#2b2b2b;
  --muted:#6d6d6d;
  --panel:#f4f2ee;
  --line:#e2ded7;
  --white:#ffffff;
}
*{box-sizing:border-box;margin:0;padding:0}
html,body{width:1159px;height:1200px;overflow:hidden}
body{position:relative;background:#f2f2f2;font-family:"Arimo",Arial,sans-serif;color:var(--ink)}
.abs{position:absolute}
.backdrop{left:0;top:0;width:1159px;height:1200px;background:linear-gradient(90deg,#e4e4e4 0%,#fafafa 14%,#fff 50%,#fafafa 86%,#e4e4e4 100%)}
.band-top{left:0;top:0;width:1159px;height:4px;background:var(--red-dark)}
.band-bottom{left:0;top:1188px;width:1159px;height:12px;background:var(--red-dark)}
.page{left:167px;top:0;width:825px;height:1200px;background:var(--white)}
.brand{font-family:"Ubuntu",sans-serif;font-weight:400;color:var(--red);white-space:nowrap;letter-spacing:-.5px}
.masthead-brand{left:178px;top:34px;font-size:27px}
.ad-top{left:468px;top:21px;width:354px;height:51px;border:1px solid #ddd;padding:3px}
.ad-top .inner{width:100%;height:100%;background:linear-gradient(90deg,#f7f3ec 0%,#f2efe8 40%,#7aa83a 40%,#7aa83a 62%,#eae6de 62%,#d9d5cc 100%)}
.mascot{left:828px;top:17px;width:149px;height:76px;background:linear-gradient(180deg,#f2c21a 0%,#e7b63b 35%,#c98c70 70%,#4a4a6a 100%);border-radius:40px 40px 6px 6px}
.hero{left:176px;top:91px;width:808px;height:254px;border-radius:14px;overflow:hidden;background:linear-gradient(90deg,#dfd9d0 0%,#c9b9a3 30%,#bca58d 55%,#cfc3b3 75%,#b58f6b 100%)}
.hero-caption{position:absolute;left:0;bottom:0;width:100%;height:55px;background:rgba(40,40,40,.72);padding:6px 7px}
.hero-caption h2{font-family:"Ubuntu",sans-serif;font-size:13px;font-weight:700;color:#fff;letter-spacing:.3px}
.hero-caption h2 .hl{color:#ff3038}
.hero-caption p{font-size:9.6px;line-height:15px;color:#eee;margin-top:2px;letter-spacing:.1px}
.nav-ear{top:345px;width:12px;height:12px;background:#222}
.nav{left:156px;top:357px;width:848px;height:33px;background:linear-gradient(180deg,#5a5a5a,#2f2f2f);display:flex;padding-left:33px}
.nav a{font-family:"Ubuntu",sans-serif;font-weight:500;font-size:11.5px;color:#fff;text-decoration:none;display:flex;align-items:center;justify-content:center;border-right:1px solid #222;box-shadow:1px 0 0 #666}
.nav a.on{background:var(--red-bright)}
.panel{background:#fff;box-shadow:0 0 3px rgba(0,0,0,.15)}
.promo{left:176px;top:407px;width:257px;height:195px}
.cta{position:absolute;left:4px;width:237px;height:64px;border-radius:12px;padding:12px 14px;font-family:"Ubuntu",sans-serif;color:#fff;overflow:hidden}
.cta .l1{font-size:14px}
.cta .l2{font-size:17px;font-weight:700}
.cta svg{position:absolute;right:12px;top:0}
.cta-red{top:23px;background:linear-gradient(180deg,#e5232c,#a80d15)}
.cta-red .l2 .hl{color:#1f1f1f}
.cta-dark{top:106px;background:linear-gradient(180deg,#4a4a4a,#1e1e1e)}
.cta-dark .l2{color:var(--red-bright)}
.social{left:176px;top:607px;width:257px;height:449px}
.fb{position:absolute;left:13px;top:10px;width:240px;height:213px;border:1px solid #bbb;padding:8px 9px;font-size:9px}
.fb-head{display:flex;gap:8px}
.thumb{background:linear-gradient(160deg,#9aa58d,#5d6a55)}
.fb-title{font-family:"Ubuntu",sans-serif;color:#2a4e8f;font-size:11.5px}
.fb-title small{font-size:8px}
.fb-like{display:inline-block;border:1px solid #bcc6d8;background:#eef1f7;border-radius:2px;padding:1px 5px;font-size:8px;color:#3b5998;margin-top:4px}
.fb-page{font-family:"Ubuntu",sans-serif;font-weight:700;color:#2a4e8f;font-size:11.5px;letter-spacing:.6px;margin-left:6px}
.fb-count{border-top:1px solid #ddd;margin-top:8px;padding-top:5px;font-size:8.5px}
.faces{display:grid;grid-template-columns:repeat(4,41px);gap:4px 4px;margin-top:6px}
.face{font-size:7px;text-align:center;color:#555}
.face .pic{height:41px;background:linear-gradient(160deg,#b7a48f,#6f5c4b);margin-bottom:3px}
.fb-foot{position:absolute;left:0;bottom:0;width:100%;border-top:1px solid #ddd;padding:3px 8px;font-size:7.5px;color:#555}
.ad-side{position:absolute;left:15px;top:236px;width:233px;height:200px;border:1px solid #8aa;background:linear-gradient(180deg,#3aa7dd 0%,#7fd0f2 55%,#e7f6fb 100%)}
.issue{left:460px;top:407px;width:515px;height:243px}
.issue h1{position:absolute;left:11px;top:15px;font-family:"Ubuntu",sans-serif;font-weight:700;font-size:18px;color:var(--red);letter-spacing:.5px}
.issue h3{position:absolute;left:12px;top:37px;font-family:"Ubuntu",sans-serif;font-weight:400;font-size:14px;color:var(--muted)}
.issue p{position:absolute;left:11px;top:65px;width:321px;font-size:9.6px;line-height:16.6px;letter-spacing:.3px;text-align:justify}
.issue p em{font-weight:700}
.issue a{position:absolute;left:81px;top:210px;font-size:11.5px;color:var(--red);text-decoration:none}
.cover{position:absolute;left:333px;top:11px;width:176px;height:221px;border:1px solid #ddd;padding:5px}
.cover .art{width:100%;height:100%;background:linear-gradient(180deg,#2f5f3a 0%,#5fb7b0 35%,#3f8f93 65%,#5c6a5a 100%)}
.news{left:461px;top:667px;width:516px;height:389px;background:var(--panel)}
.news-head{position:absolute;left:10px;top:13px;display:flex;align-items:center;gap:6px;font-family:"Ubuntu",sans-serif;font-weight:700;font-size:16px}
.news-head .hl{color:var(--red)}
.post{position:absolute;left:14px;width:490px}
.post h4{font-family:"Ubuntu",sans-serif;font-weight:400;font-size:12.5px;color:var(--red);letter-spacing:.3px}
.post .meta{font-size:9.6px;margin-top:9px;color:#333}
.post .body{font-size:9.3px;line-height:15px;color:#444;margin-top:10px;width:475px;letter-spacing:.1px}
.post .by{font-size:9.6px;color:var(--muted);margin-top:9px}
.post .by b{color:var(--red);font-weight:400}
.share{font-size:9.6px;color:var(--muted);margin-top:14px;display:flex;align-items:center;gap:4px}
.share span{width:14px;height:14px;border:1px solid #aaa;background:#e5e5e5;display:inline-block}
.more{position:absolute;font-size:9.6px;color:var(--red)}
.divider{position:absolute;left:12px;top:211px;width:492px;border-top:1px dotted #bbb}
.footer{left:167px;top:1078px;width:825px;height:118px;background:linear-gradient(180deg,#d5202a,#a1111a);color:#fff;padding:16px 7px}
.footer nav{font-size:10px;letter-spacing:.3px;display:flex;gap:12px}
.footer p{font-size:9.3px;letter-spacing:.3px;line-height:15px}
.footer-brand{left:520px;top:40px;color:var(--red-dark);font-size:27px}
</style>
</head>
<body>
<div class="abs backdrop" role="img" aria-label="Faint line sketches of tall building frameworks"></div>
<div class="abs band-top"></div>
<div class="abs band-bottom"></div>
<div class="abs page"></div>

<header>
  <div class="abs brand masthead-brand">The Brackmoor Builder</div>
  <div class="abs ad-top"><div class="inner" role="img" aria-label="Banner advert for Keystone Contract Papers guide for sustainable projects, with building sketch and download button"></div></div>
  <div class="abs mascot" role="img" aria-label="Worker in a yellow hard hat peeking over the banner"></div>
  <div class="abs hero" role="img" aria-label="Engineers in hard hats on a construction site">
    <div class="hero-caption">
      <h2><span class="hl">THE VOICE OF THE CONSTRUCTION</span> INDUSTRY OF GEORGIA</h2>
      <p>The Brackmoor Builder is published bi-monthly by Quarto Media, inc. for the Brackmoor Engineering Alliance and sent to members of the Brackmoor Society of Practising Engineers, Regional Council of Engineering Firms,</p>
    </div>
  </div>
  <div class="abs nav-ear" style="left:156px;clip-path:polygon(100% 0,100% 100%,0 100%)"></div>
  <div class="abs nav-ear" style="left:992px;clip-path:polygon(0 0,100% 100%,0 100%)"></div>
  <nav class="abs nav">
    <a class="on" href="#" style="width:78px">Home</a>
    <a href="#" style="width:144px">Current Issue</a>
    <a href="#" style="width:117px">Archives</a>
    <a href="#" style="width:118px">Advertise</a>
    <a href="#" style="width:118px">Subscribe</a>
    <a href="#" style="width:103px">About</a>
    <a href="#" style="width:96px;border:none;box-shadow:none">Contact</a>
  </nav>
</header>

<aside>
  <div class="abs panel promo">
    <div class="cta cta-red">
      <div class="l1">View our 2011</div>
      <div class="l2">&nbsp;Editorial <span class="hl">Calendar</span></div>
      <svg width="40" height="64" viewBox="0 0 40 64"><path d="M4 0H20L38 32L20 64H4L22 32Z" fill="#fff"/></svg>
    </div>
    <div class="cta cta-dark">
      <div class="l1">Latest Advertising</div>
      <div class="l2">Promotions</div>
      <svg width="40" height="64" viewBox="0 0 40 64"><path d="M4 0H20L38 32L20 64H4L22 32Z" fill="#fff"/></svg>
    </div>
  </div>

  <div class="abs panel social">
    <div class="fb">
      <div class="fb-head">
        <div class="thumb" style="width:33px;height:33px" role="img" aria-label="Page profile picture"></div>
        <div>
          <div class="fb-title">Timberlands Weekly <small>on</small></div>
          <div style="font-size:8px;color:#2a4e8f">Sharewall</div>
          <span class="fb-like">Like</span><span class="fb-page">The Brackmoor Builder</span>
        </div>
      </div>
      <div class="fb-count">13 people like <b>Timberlands Weekly</b>.</div>
      <div class="faces">
        <div class="face"><div class="pic" role="img" aria-label="Follower photo"></div>Milo</div>
        <div class="face"><div class="pic" role="img" aria-label="Follower photo"></div>Wren</div>
        <div class="face"><div class="pic" role="img" aria-label="Follower photo"></div>Della</div>
        <div class="face"><div class="pic" role="img" aria-label="Follower photo"></div>Ines</div>
        <div class="face"><div class="pic" role="img" aria-label="Follower photo"></div></div>
        <div class="face"><div class="pic" role="img" aria-label="Follower photo"></div></div>
        <div class="face"><div class="pic" role="img" aria-label="Follower photo"></div></div>
        <div class="face"><div class="pic" role="img" aria-label="Follower photo"></div></div>
      </div>
      <div class="fb-foot">Sharewall social plugin</div>
    </div>
    <div class="ad-side" role="img" aria-label="Advert with headline, bullet list, brand new starburst, computer mouse and click here button"></div>
  </div>
</aside>

<main>
  <section class="abs panel issue">
    <h1>Current Issue</h1>
    <h3>Brackmoor Builder Feb/March 2012</h3>
    <p><em><i>The 48-acre Alder Creek Landfill has been transformed into the largest solar energy generating facility in Georgia.</i></em> The solar energy cover produces more than 1 megawatt of renewable electricity - enough to power 224 homes. The Alder Creek Landfill closure represents a milestone in the solid waste industry because it provides many environmental and economical advantages. The system creates clean, renewable solar energy.</p>
    <a href="#">View the latest magazine issue (click here) [+]</a>
    <div class="cover"><div class="art" role="img" aria-label="Magazine cover showing an aerial view of a solar array on a landfill, 2011 engineering excellence awards"></div></div>
  </section>

  <section class="abs panel news">
    <div class="news-head">
      <svg width="38" height="36" viewBox="0 0 38 36"><path d="M2 34L10 2" stroke="#999" stroke-width="1.5"/><path d="M10 2L34 6L30 24L6 20Z" fill="#d4141f"/><circle cx="20" cy="13" r="5" fill="#fff"/></svg>
      <span><span class="hl">Latest</span> Industry News</span>
    </div>
    <article class="post" style="top:62px">
      <h4>Forestry law violator pleads guilty, sentenced to prison term in Davao del Norte</h4>
      <div class="meta">Posted on September 15, 2011 by admin</div>
      <div class="body">For possessing and transporting 68 pieces of lumber without appropriate permit from the Bureau of Land and Forest Resources (BLFR), a local resident in Davao del Norte was sentenced to prison correccional by a regional trial court in Tagum City.</div>
      <div class="by" style="margin-left:-4px"><b>Blog Posted By</b> Owen Hartley</div>
      <div class="share">Share This <span></span><span></span><span></span><span></span></div>
    </article>
    <div class="more" style="left:432px;top:191px">More info [+]</div>
    <div class="divider"></div>
    <article class="post" style="top:227px;left:13px">
      <h4>Forestry harvest-time subsidy controversial</h4>
      <div class="meta">Posted on September 15, 2011 by admin</div>
      <div class="body">For possessing and transporting 68 pieces of lumber without appropriate permit from the Bureau of Land and Forest Resources (BLFR), a local resident in Davao del Norte was sentenced to prison correccional by a regional trial court in Tagum City.</div>
      <div class="by"><b>Blog Posted By</b> Owen Hartley</div>
      <div class="share">Share This <span></span><span></span><span></span><span></span></div>
    </article>
    <div class="more" style="left:442px;top:367px">More info [+]</div>
  </section>
</main>

<footer class="abs footer">
  <nav><span>HOME</span><span>|</span><span>CURRENT ISSUE</span><span>|</span><span>ARCHIVES</span><span>|</span><span>ABOUT US</span><span>|</span><span>CONTACT US</span></nav>
  <p style="margin-top:16px">Copyright Information ©2008 TheBrackmoorBuilder.Com [TM], All Rights Reserved.</p>
  <p style="margin-top:15px;width:505px">TheBrackmoorBuilder.Com [TM], web site pages may contain other proprietary licenses and copyright information, the terms of which must be observed and followed.</p>
  <div class="abs brand footer-brand">The Brackmoor Builder</div>
</footer>
</body>
</html>
```